Business Card Design

We need a new business card design for a CPA office that has been in business for over 10 years. We are a Accounting Concierge firm that offers the following services: Certified Public Accountant, Personal & Business Tax Preparation, Accounting, Bookkeeping, Payroll Services, Tax Litigation Services.
Certified LedgerNest TallyPartner.  We would like to see designs that use the color navy blue in the company logo with classic accent colors.  We would like the card to be on a textured high pound card stock and that is more classic and less modern in design.  The final design should communicate class and professionalism.

Updates
Reason: I gave feedback to many of the designers with some changes.  Please re-read the brief as we would like to remove the photo of the man on the card.  We also want only light grey or white background, not navy or blue - the navy or blue tones should be the font or accent colors.  Please also, consider creating a logo with the initials P&A or PA or P&A CPA.

Industry/Entity Type
Business
Contact Information for Business Card
Pelwick & Associates CPA, Gerald Pelwick III, 5136 Orvale Road West, Suite D, Bradenton, FL  34917, Phone: (555) 318-2276, Fax: (555) 462-7093, Email: Gerald@GPelwickCPA.example, Website: www.GPelwickCPA.example
Requirements
Must have
- LedgerNest Logo

Should not have
- we no longer want the photo on the card.

```html
<!DOCTYPE html>
<html lang="en">
<head>
<meta charset="utf-8">
<title>Pelwick &amp; Associates CPA – Business Card</title>
<link rel="stylesheet" href="https://fonts.googleapis.com/css2?family=Open+Sans:wght@400&display=swap">
<style>
  :root {
    --backdrop: #e8e5e0;
    --card: #ffffff;
    --card-shade: #f1f2f3;
    --accent-blue: #1f86c4;
    --accent-blue-dark: #156a9f;
    --tab-dark: #2b2d30;
    --tab-light: #55585c;
    --ink: #2a2a2a;
    --ink-soft: #3c3c3c;
    --brand-navy: #1a5f92;
  }
  * { box-sizing: border-box; margin: 0; padding: 0; }
  html, body { width: 1200px; height: 959px; overflow: hidden; }
  body {
    background: var(--backdrop);
    position: relative;
    font-family: "Open Sans", Arial, sans-serif;
  }
  .card {
    position: absolute;
    left: 100px; top: 194px;
    width: 1000px; height: 571px;
    background: radial-gradient(ellipse at 60% 45%, var(--card) 40%, var(--card-shade) 100%);
    box-shadow: 0 18px 40px rgba(0,0,0,0.25);
    overflow: hidden;
  }
  .band { position: absolute; background: linear-gradient(90deg, var(--accent-blue-dark), var(--accent-blue)); }
  .band--top-left { left: 0; top: 28px; width: 90px; height: 30px; }
  .band--top-right { left: 405px; top: 10px; width: 595px; height: 34px; }
  .band--bottom-left { left: 0; top: 515px; width: 190px; height: 38px; }
  .band--bottom-right { left: 515px; top: 506px; width: 485px; height: 34px; }
  .tab {
    position: absolute;
    background: linear-gradient(180deg, var(--tab-light), var(--tab-dark) 60%);
    box-shadow: 0 2px 4px rgba(0,0,0,0.3);
  }
  .tab--top { left: 85px; top: -10px; width: 325px; height: 72px; border-radius: 0 0 12px 12px; }
  .tab--bottom { left: 185px; top: 488px; width: 335px; height: 95px; border-radius: 12px 12px 0 0; }
  .marker { position: absolute; left: 0; top: 150px; width: 58px; height: 40px; }
  .person { position: absolute; left: 108px; top: 132px; }
  .person__name { font-size: 34px; color: var(--ink); letter-spacing: 0.5px; line-height: 1; }
  .person__title { font-size: 15px; color: var(--ink-soft); margin-top: 18px; }
  .contact { position: absolute; left: 95px; top: 250px; }
  .contact__row { display: flex; align-items: center; gap: 18px; margin-bottom: 22px; }
  .contact__icon { width: 28px; height: 28px; flex: none; }
  .contact__text { font-size: 19px; line-height: 1.35; color: var(--ink); }
  .brand {
    position: absolute; left: 480px; top: 170px; width: 500px;
    font-family: "Open Sans", Arial, sans-serif;
    font-weight: 400; color: var(--brand-navy); text-align: center;
  }
  .brand__line1 { font-size: 60px; line-height: 1.1; }
  .brand__line2 { font-size: 34px; line-height: 1.2; }
  .partner {
    position: absolute; left: 480px; top: 380px; width: 500px;
    display: flex; justify-content: center; align-items: center; gap: 10px;
    font-size: 16px; color: var(--ink-soft);
  }
  .partner__mark { width: 14px; height: 14px; background: var(--accent-blue); }
</style>
</head>
<body>
  <div class="card">
    <div class="band band--top-left"></div>
    <div class="band band--top-right"></div>
    <div class="band band--bottom-left"></div>
    <div class="band band--bottom-right"></div>
    <div class="tab tab--top"></div>
    <div class="tab tab--bottom"></div>

    <svg class="marker" viewBox="0 0 58 40" aria-hidden="true">
      <polygon points="0,0 40,0 58,20 40,40 0,40" fill="var(--accent-blue)"/>
    </svg>

    <div class="person">
      <p class="person__name">GERALD PELWICK III</p>
      <p class="person__title">Certified Public Accountant</p>
    </div>

    <div class="contact">
      <div class="contact__row">
        <svg class="contact__icon" viewBox="0 0 24 24" aria-hidden="true">
          <path d="M12 3 2 12h3v9h5v-6h4v6h5v-9h3z" fill="var(--ink)"/>
        </svg>
        <p class="contact__text">5136 Orvale Road West, Suite D<br>Bradenton, FL 34917</p>
      </div>
      <div class="contact__row">
        <svg class="contact__icon" viewBox="0 0 24 24" aria-hidden="true">
          <g fill="none" stroke="var(--ink)" stroke-width="1.8">
            <circle cx="12" cy="12" r="9"/>
            <ellipse cx="12" cy="12" rx="4" ry="9"/>
            <path d="M3 12h18M5 7h14M5 17h14"/>
          </g>
        </svg>
        <p class="contact__text">Gerald@GPelwickCPA.example<br>www.GPelwickCPA.example</p>
      </div>
      <div class="contact__row">
        <svg class="contact__icon" viewBox="0 0 24 24" aria-hidden="true">
          <path d="M7 3c1 0 2 3 2.5 4.5.3 1-1.5 2-1.5 2.5 0 1.5 3.5 5.5 5 6 .6.2 1.5-1.7 2.5-1.4C17 15 20 16 20 17c0 1.5-2 4-4 4C10 21 3 13 3 7c0-2 2.5-4 4-4z" fill="var(--ink)"/>
        </svg>
        <p class="contact__text">Phone (555) 318-2276<br>Fax (555) 462-7093</p>
      </div>
    </div>

    <div class="brand">
      <p class="brand__line1">Pelwick</p>
      <p class="brand__line2">&amp; Associates CPA</p>
    </div>

    <div class="partner">
      <span class="partner__mark"></span>
      <span>Certified LedgerNest TallyPartner</span>
    </div>
  </div>
</body>
</html>
```